Vision Mission Values Layout for Displaying

We our looking for a format or template that we can transfer onto canvas, metal, or picture to display in our front lobby, break room, and conference room. We would like to incorporate our company logo and colors. Red Black & White. We would like them all displayed on the same canvas, sheet metal, or picture. This is our first time using this site we are hoping to use this site for our web design and possible re design our logo. When we walk into other businesses we see their vision, mission, and values displayed. We are looking for something similar.

Industry/Entity Type

It Company

Requirements
Must have
• Company Name and Logo
• Mission Vision and Values
Nice to have
• the definitions
Should not have
• Contact Information

```html
<!DOCTYPE html>
<html lang="en">
<head>
<meta charset="utf-8">
<title>Norvane Industrial Fabrication – Vision, Mission, Values</title>
<link rel="stylesheet" href="https://fonts.googleapis.com/css2?family=Ubuntu:wght@500;700&display=swap">
<style>
  :root {
    --red: #e8202a;
    --red-soft: #f0494e;
    --black: #111111;
    --charcoal: #2b2b2b;
    --white: #ffffff;
    --figure-tone: #f4c9cb;
  }
  * { margin: 0; padding: 0; box-sizing: border-box; }
  html, body { width: 848px; height: 1200px; overflow: hidden; }
  body { font-family: "Ubuntu", Arial, sans-serif; color: var(--white); background: var(--charcoal); }

  .poster { position: relative; width: 848px; height: 1200px; overflow: hidden;
    background: radial-gradient(ellipse 70% 50% at 35% 40%, #5a5a5a 0%, #3a3a3a 45%, #222 100%); }

  .stripe-band { position: absolute; left: 558px; top: 0; width: 290px; height: 690px;
    background: linear-gradient(90deg, #e9e9e9 0%, #d6d6d6 45%, var(--red) 70%, var(--red-soft) 100%); }
  .floor { position: absolute; left: 0; top: 690px; width: 848px; height: 510px;
    background: linear-gradient(180deg, #5b5b5b 0%, #8a8a8a 45%, #3a3a3a 100%); }

  .brand { position: absolute; left: 571px; top: 34px; width: 231px; height: 152px;
    background: var(--white); display: flex; align-items: center; justify-content: center; gap: 10px; padding: 0 14px; }
  .brand-mark { width: 16px; height: 16px; background: var(--red); flex: none; }
  .brand-name { font-weight: 700; font-size: 22px; line-height: 1.15; color: var(--black); text-transform: uppercase; }

  .statement-icon { position: absolute; left: 30px; }
  .statement-title { position: absolute; left: 130px; font-weight: 700; font-size: 52px; line-height: 52px; color: var(--red); letter-spacing: 1px; }
  .statement-text { position: absolute; left: 132px; font-weight: 500; color: var(--white); }
  .vision-icon { top: 228px; }
  .vision-title { top: 226px; }
  .vision-text { top: 278px; font-size: 20px; line-height: 27.6px; }
  .mission-icon { top: 374px; }
  .mission-title { top: 383px; }
  .mission-text { top: 437px; font-size: 21.6px; line-height: 27.3px; }

  .values-title { position: absolute; left: 34px; top: 612px; font-weight: 700; font-size: 56px; line-height: 56px; color: var(--red); letter-spacing: 1px; }

  .value-card { position: absolute; width: 380px; height: 142px; background: var(--red); border-radius: 24px; }
  .value-figure { position: absolute; left: 8px; top: 8px; width: 84px; height: 126px; border-radius: 14px;
    background: linear-gradient(180deg, var(--figure-tone), #e9959a); opacity: .55; }
  .value-name { position: absolute; left: 96px; top: 9px; font-weight: 700; font-size: 22px; line-height: 26px; }
  .value-terms { position: absolute; left: 96px; top: 48px; font-weight: 500; font-size: 11.5px; line-height: 15.6px; white-space: nowrap; }
  .col-left { left: 34px; } .col-right { left: 428px; }
  .row-1 { top: 686px; } .row-2 { top: 854px; } .row-3 { top: 1022px; }
</style>
</head>
<body>
<main class="poster">
  <div class="floor" role="img" aria-label="Decorative perspective floor in grey, white and black tones"></div>
  <div class="stripe-band" role="img" aria-label="Decorative vertical band in white, black and red tones"></div>

  <div class="brand">
    <span class="brand-mark"></span>
    <span class="brand-name">Norvane Industrial Fabrication</span>
  </div>

  <svg class="statement-icon vision-icon" width="90" height="52" viewBox="0 0 90 52" aria-hidden="true">
    <path d="M2 26 Q45 -10 88 26 Q45 62 2 26Z" fill="#fff"/>
    <circle cx="45" cy="26" r="16" fill="#111"/>
    <circle cx="45" cy="26" r="8" fill="#fff"/>
    <circle cx="41" cy="22" r="3" fill="#111"/>
  </svg>
  <h2 class="statement-title vision-title">VISION:</h2>
  <p class="statement-text vision-text">Exceptional People Fabricating<br>Inspiring Projects</p>

  <svg class="statement-icon mission-icon" width="86" height="68" viewBox="0 0 86 68" aria-hidden="true">
    <g fill="none" stroke="#fff" stroke-width="7">
      <path d="M52 12 A28 28 0 1 0 66 38"/>
      <path d="M46 26 A14 14 0 1 0 54 38"/>
    </g>
    <circle cx="40" cy="38" r="5" fill="#fff"/>
    <path d="M40 38 L70 12" stroke="#fff" stroke-width="4"/>
    <path d="M66 6 L70 12 L78 14 L84 8 L76 6 L74 0Z" fill="#fff"/>
  </svg>
  <h2 class="statement-title mission-title">MISSION:</h2>
  <p class="statement-text mission-text">Our Mission is to be the<br>“Steel Fabricator of Choice”<br>through innovative solutions and<br>the consistent delivery of a high<br>quality customer experience!</p>

  <h2 class="values-title">VALUES:</h2>

  <article class="value-card col-left row-1">
    <div class="value-figure" role="img" aria-label="White figure of a worker with a handshake icon"></div>
    <h3 class="value-name">Integrity:</h3>
    <p class="value-terms">Consistency, Fairness, Commitment,<br>Ethical, Moral, Do What We Say We Are<br>Going to Do, Do the Right Thing Always</p>
  </article>
  <article class="value-card col-right row-1">
    <div class="value-figure" role="img" aria-label="White figure of a worker with a magnifying glass icon"></div>
    <h3 class="value-name">Customer-Focused:</h3>
    <p class="value-terms">Exceeding Requirements, Communication,<br>Passion to Serve, Understanding of<br>Customer’s Needs, Solutions-Oriented,<br>Dedicated to the Success of Others,<br>Responsive, Sense of Urgency</p>
  </article>
  <article class="value-card col-left row-2">
    <div class="value-figure" role="img" aria-label="White figure of a worker with an award ribbon icon"></div>
    <h3 class="value-name">Excellence:</h3>
    <p class="value-terms">High Quality, Drive, Talent, Best, the<br>Gold Standard, Being your Best</p>
  </article>
  <article class="value-card col-right row-2">
    <div class="value-figure" role="img" aria-label="White figure of a worker with a puzzle piece icon"></div>
    <h3 class="value-name">Collaboration:</h3>
    <p class="value-terms">Teamwork, Engagement, Partnership,<br>Relationship, Listening, Communication,<br>Sharing, Collective, Community</p>
  </article>
  <article class="value-card col-left row-3">
    <div class="value-figure" role="img" aria-label="White figure of a worker with a flame icon"></div>
    <h3 class="value-name">Passion:</h3>
    <p class="value-terms">Driven, Spirited, Enthusiasm,<br>Competitive, Enjoyment, Energy</p>
  </article>
  <article class="value-card col-right row-3">
    <div class="value-figure" role="img" aria-label="White figure of a worker with a light bulb and gears icon"></div>
    <h3 class="value-name">Innovation:</h3>
    <p class="value-terms">Creativity, Cutting-Edge, Smart, LEAN,<br>Leading, Performance, Continuous<br>Improvement</p>
  </article>
</main>
</body>
</html>
```